Investment company needing business card

We are wanting a business card which looks sharp and easy on the eye. We are thinking of having a business card with the logo embossed on it, to really make it stand out. We will only have a small amount of information of the business card, person's name, position, email address and phone number

Contact Information for Business Card

Danica Pruett
Executive Assistant
+64 21 547 3162
danicap@harwellcapital.co.nz

Requirements
Must have
• Embossed logo
Should not have
• Not to be busy

```html
<!DOCTYPE html>
<html lang="en">
<head>
<meta charset="utf-8">
<title>Harwell Capital — Business Card</title>
<link href="https://fonts.googleapis.com/css2?family=Roboto:wght@400;500;700&display=swap" rel="stylesheet">
<style>
  :root {
    --backdrop: #2b2b2b;
    --brand-green: #22b573;
    --brand-green-light: #2cc281;
    --brand-grey: #636466;
    --card-white: #ffffff;
    --ink-dark: #3a3a3a;
  }
  * { box-sizing: border-box; margin: 0; padding: 0; }
  html, body {
    width: 1200px; height: 900px; overflow: hidden;
    background: var(--backdrop);
    font-family: "Roboto", Arial, sans-serif;
  }
  .canvas { position: relative; width: 1200px; height: 900px; }

  .card {
    position: absolute;
    width: 600px; height: 343px;
    overflow: hidden;
    box-shadow: 0 14px 30px rgba(0,0,0,.45);
  }
  .card--front { left: 80px; top: 90px; background: var(--brand-green); }
  .card--back  { left: 520px; top: 467px; background: var(--card-white); }

  .wordmark {
    position: absolute;
    display: flex; align-items: center; gap: 12px;
    font-weight: 700; text-transform: uppercase; letter-spacing: .06em;
    white-space: nowrap;
  }
  .wordmark__square { display: block; flex: none; }
  .card--front .wordmark {
    left: 50%; top: 50%; transform: translate(-50%, -50%);
    color: var(--card-white); font-size: 40px;
  }
  .card--front .wordmark__square { width: 44px; height: 44px; background: var(--brand-grey); }
  .card--back .wordmark {
    left: 40px; top: 52px;
    color: var(--brand-green); font-size: 24px;
  }
  .card--back .wordmark__square { width: 28px; height: 28px; background: var(--brand-green); }

  .card__band {
    position: absolute; left: 0; right: 0; bottom: 0; height: 190px;
    background: linear-gradient(160deg, var(--brand-green-light), var(--brand-green));
  }

  .holder {
    position: absolute; right: 44px; top: 40px; text-align: right;
  }
  .holder__name { color: var(--brand-green); font-weight: 700; font-size: 21px; }
  .holder__role { color: var(--ink-dark); font-size: 12px; margin-top: 2px; }

  .contacts {
    position: absolute; right: 32px; bottom: 60px;
    list-style: none; text-align: right;
    color: var(--card-white); font-size: 16px;
  }
  .contacts li {
    display: flex; align-items: center; justify-content: flex-end; gap: 10px;
    margin-top: 8px;
  }
  .contacts svg { width: 22px; height: 22px; flex: none; }
</style>
</head>
<body>
<main class="canvas">
  <section class="card card--front" aria-label="Card front">
    <div class="wordmark"><span class="wordmark__square"></span>Harwell Capital</div>
  </section>

  <section class="card card--back" aria-label="Card back">
    <div class="card__band" role="img" aria-label="Green flowing wave decoration with grey and white accent stripes"></div>

    <div class="wordmark"><span class="wordmark__square"></span>Harwell Capital</div>

    <div class="holder">
      <p class="holder__name">Danica Pruett</p>
      <p class="holder__role">Executive Assistant</p>
    </div>

    <ul class="contacts">
      <li>+64 21 547 3162
        <svg viewBox="0 0 22 22" aria-hidden="true"><rect width="22" height="22" fill="var(--card-white)"/><path d="M7 5l3 3-2 2c1 2 2 3 4 4l2-2 3 3-2 2c-5 0-10-5-10-10z" fill="var(--brand-green)"/></svg>
      </li>
      <li>danicap@harwellcapital.co.nz
        <svg viewBox="0 0 22 22" aria-hidden="true"><rect width="22" height="22" fill="var(--card-white)"/><rect x="4" y="6" width="14" height="10" fill="none" stroke="var(--brand-green)" stroke-width="1.6"/><path d="M4 6l7 6 7-6" fill="none" stroke="var(--brand-green)" stroke-width="1.6"/></svg>
      </li>
    </ul>
  </section>
</main>
</body>
</html>
```